Construction Company

Design a clutter free business card, it can be double-sided utilizing the logo for BDN Ltd simple with all relevant contact information.

Please also a letterhead design to function for the purposes of invoicing, all mail requirements, with header to be distinctive while the footer ties page together and incorporates all necessary information.

For now, please use generic / dummy text and when a winner is selected, I will disclose the contact information.

Hi Designers! Please read the updated brief which includes the design of a business card and letterhead. Thank you!

```html
<!DOCTYPE html>
<html lang="en">
<head>
<meta charset="utf-8">
<title>BDN Ltd – Letterhead &amp; Business Card</title>
<link href="https://fonts.googleapis.com/css2?family=Lato:wght@300;400;700&family=Open+Sans:wght@400;600;700&family=Pinyon+Script&display=swap" rel="stylesheet">
<style>
  :root{
    --navy:#1f3480;
    --gold:#b8982e;
    --gold-deep:#ad8f2c;
    --paper:#f3f3f3;
    --card:#f6f6f6;
    --ink:#4a4a4a;
    --ink-dark:#1c1c1c;
    --bg:#e6e6e6;
  }
  *{margin:0;padding:0;box-sizing:border-box}
  html,body{width:1200px;height:960px;overflow:hidden;background:var(--bg)}
  body{position:relative;font-family:'Lato',sans-serif;color:var(--ink)}

  /* ---------- Letterhead ---------- */
  .letterhead{position:absolute;left:90px;top:80px;width:620px;height:800px;background:var(--paper);box-shadow:0 2px 10px rgba(0,0,0,.12);overflow:hidden}
  .brand{position:absolute;display:flex;align-items:center;gap:8px;font-family:'Open Sans',sans-serif;font-weight:700;color:var(--navy);letter-spacing:.5px}
  .brand .dot{display:block;border-radius:50%;background:var(--navy)}
  .letterhead .brand{left:48px;top:52px;font-size:34px}
  .letterhead .brand .dot{width:14px;height:14px}

  .sender{position:absolute;right:48px;top:34px;padding-left:13px;border-left:1.5px solid var(--gold);font-family:'Open Sans',sans-serif;font-style:normal;font-size:10.5px;line-height:12.5px;color:var(--ink-dark)}
  .sender .contact-list{margin-top:5px;list-style:none}
  .contact-list li{display:flex;align-items:center;gap:6px}
  .contact-list svg{flex:none;fill:var(--navy)}

  .letter{position:absolute;left:72px;top:160px;width:475px;font-size:10px;line-height:14.2px;font-weight:400;color:var(--ink)}
  .letter .date{margin-bottom:16px}
  .letter .recipient{margin-bottom:28px}
  .letter .recipient strong{font-weight:700;color:var(--ink-dark)}
  .letter .salutation{margin-bottom:14px}
  .letter p.body{text-align:justify;margin-bottom:14px}
  .letter .closing{margin-top:34px}
  .letter .signature{font-family:'Pinyon Script',cursive;font-size:22px;color:var(--ink-dark);margin-top:4px;margin-left:6px}

  .footer-wave{position:absolute;left:0;bottom:0;width:620px;height:56px}
  .letterhead .web{position:absolute;right:78px;bottom:14px;font-family:'Open Sans',sans-serif;font-size:10.5px;letter-spacing:1.6px;color:#fff}
  .web .domain{color:var(--gold)}

  /* ---------- Business cards ---------- */
  .card{position:absolute;left:760px;width:380px;height:216px;box-shadow:0 2px 8px rgba(0,0,0,.14);overflow:hidden}
  .card-front{top:250px;background:var(--card)}
  .card-back{top:494px;background:var(--gold-deep)}

  .card-front .brand{left:26px;top:84px;font-size:26px}
  .card-front .brand .dot{width:11px;height:11px}
  .card-details{position:absolute;left:190px;top:58px;padding-left:14px;border-left:1.2px solid var(--gold);font-family:'Open Sans',sans-serif;color:var(--ink-dark);font-size:8px;line-height:10px}
  .card-details .name{font-size:11.5px;font-weight:700;color:var(--navy);line-height:13px}
  .card-details .title{font-size:8px;color:var(--gold);margin-bottom:12px}
  .card-details .address{margin-bottom:6px}
  .card-details .contact-list{list-style:none}
  .card-wave{position:absolute;left:0;bottom:0;width:380px;height:38px}
  .card-front .web{position:absolute;right:52px;bottom:8px;font-family:'Open Sans',sans-serif;font-size:8.5px;color:#fff}

  .card-back .brand{left:0;right:0;top:70px;justify-content:center;color:#fff;font-size:38px;font-weight:700}
  .card-back .brand .dot{width:15px;height:15px;background:#fff}
  .card-back .web{position:absolute;left:0;right:0;top:176px;text-align:center;font-family:'Open Sans',sans-serif;font-size:8px;letter-spacing:1.2px;color:#fff}
</style>
</head>
<body>

<section class="letterhead" aria-label="BDN Ltd letterhead">
  <div class="brand"><span class="dot"></span>BDN Ltd</div>

  <address class="sender">
    BDN Ltd<br>Suite 880 Harbor Lane<br>Region, Zip 5678, Country
    <ul class="contact-list">
      <li><svg width="8" height="8" viewBox="0 0 10 10"><path d="M2 0.5l2 2-1 1.2c.6 1.3 1.7 2.4 3 3l1.2-1 2 2-1.4 1.6C4.5 9.2.8 5.5.5 1.9z"/></svg>410.555.0132</li>
      <li><svg width="8" height="8" viewBox="0 0 10 10"><rect x="2.5" y="0.5" width="5" height="3"/><rect x="0.5" y="3.5" width="9" height="4" rx="1"/><rect x="2.5" y="6.5" width="5" height="3"/></svg>410.555.0179</li>
      <li><svg width="8" height="8" viewBox="0 0 10 10"><path d="M0.5 2h9v6h-9z M0.5 2l4.5 3.5 4.5-3.5" fill="none" stroke="#1f3480" stroke-width="1.2"/></svg>contact@bdnltd.com</li>
    </ul>
  </address>

  <article class="letter">
    <div class="date">01 January 2050</div>
    <div class="recipient"><strong>Company (Pvt) Ltd.</strong><br>PO Box 4721 Elmwood Rd<br>Sample City Country 4721</div>
    <div class="salutation">Dear Martin Caldwell,</div>
    <p class="body">Lorem ipsum dolor sit amet, consectetuer adipiscing elit, sed diam nonummy nibh euismod tincidunt ut laoreet dolore magna aliquam erat volutpat. Ut wisi enim ad minim veniam, quis nostrud exerci tation ullamcorper suscipit lobortis nisl ut aliquip ex ea commodo consequat. Duis dolore te feugait nulla facilisi. Nam liber tempor cum soluta nobis eleifend option congue nihil imperdiet doming id quod mazim placerat facer possim assum. Lorem ipsum dolor sit amet, consectetuer adipiscing elit, sed diam nonummy nibh euismod tincidunt ut laoreet dolore magna aliquam erat volutpat. Ut wisi enim ad minim veniam, quis nostrud exerci tation ullamcorper suscipit lobortis nisl ut aliquip ex ea commodo consequat.</p>
    <p class="body">Consectetuer adipiscing elit, sed diam nonummy nibh euismod tincidunt ut laoreet dolore magna aliquam erat volutpat. Ut wisi enim ad minim veniam, quis nostrud exerci tation ullamcorper suscipit lobortis nisl ut aliquip ex ea commodo consequat. Consectetuer adipiscing elit, sed diam nonummy nibh euismod tincidunt ut laoreet dolore magna aliquam erat volutpat. Ut wisi enim ad minim veniam, quis nostrud exerci tation ullamcorper suscipit lobortis nisl ut aliquip ex ea commodo consequat.</p>
    <p class="body">Consectetuer adipiscing elit, sed diam nonummy nibh euismod tincidunt ut laoreet dolore magna aliquam erat volutpat. Ut wisi enim ad minim veniam, quis nostrud exerci tation ullamcorper suscipit lobortis nisl ut aliquip ex ea commodo consequat. Consectetuer adipiscing elit, sed diam nonummy nibh euismod tincidunt ut laoreet dolore magna aliquam erat volutpat. Ut wisi enim ad minim veniam, quis nostrud exerci tation ullamcorper suscipit lobortis nisl ut aliquip ex ea commodo consequat.</p>
    <div class="closing">Sincerely Yours</div>
    <div class="signature">Thomas Edward Lane</div>
  </article>

  <svg class="footer-wave" viewBox="0 0 620 56" preserveAspectRatio="none" aria-hidden="true">
    <path d="M0 4 C120 30 260 40 380 22 C470 8 540 -2 620 12 L620 56 L0 56 Z" fill="#b8982e"/>
    <path d="M0 14 C140 40 270 46 380 30 C470 16 540 8 620 20 L620 56 L0 56 Z" fill="#ffffff"/>
    <path d="M0 18 C140 44 280 50 390 34 C480 20 545 12 620 22 L620 56 L0 56 Z" fill="#b8982e"/>
    <path d="M0 24 C150 52 290 54 400 38 C490 24 550 16 620 26 L620 56 L0 56 Z" fill="#1f3480"/>
  </svg>
  <div class="web">www.<span class="domain">bdnltd</span>.com</div>
</section>

<section class="card card-front" aria-label="Business card front">
  <div class="brand"><span class="dot"></span>BDN Ltd</div>
  <div class="card-details">
    <div class="name">Daniel Foster</div>
    <div class="title">Founder &amp; CEO</div>
    <div class="address">Suite 880 Harbor Lane<br>Region, Zip 5678, Country</div>
    <ul class="contact-list">
      <li><svg width="6" height="6" viewBox="0 0 10 10"><path d="M2 0.5l2 2-1 1.2c.6 1.3 1.7 2.4 3 3l1.2-1 2 2-1.4 1.6C4.5 9.2.8 5.5.5 1.9z"/></svg>410.555.0132</li>
      <li><svg width="6" height="6" viewBox="0 0 10 10"><rect x="2.5" y="0.5" width="5" height="3"/><rect x="0.5" y="3.5" width="9" height="4" rx="1"/><rect x="2.5" y="6.5" width="5" height="3"/></svg>410.555.0179</li>
      <li><svg width="6" height="6" viewBox="0 0 10 10"><path d="M0.5 2h9v6h-9z M0.5 2l4.5 3.5 4.5-3.5" fill="none" stroke="#1f3480" stroke-width="1.4"/></svg>contact@bdnltd.com</li>
    </ul>
  </div>
  <svg class="card-wave" viewBox="0 0 380 38" preserveAspectRatio="none" aria-hidden="true">
    <path d="M0 18 C80 34 160 30 240 14 C300 2 345 2 380 10 L380 38 L0 38 Z" fill="#b8982e"/>
    <path d="M0 24 C80 38 170 34 250 18 C310 6 350 8 380 16 L380 38 L0 38 Z" fill="#1f3480"/>
  </svg>
  <div class="web">www.<b>bdnltd</b>.com</div>
</section>

<section class="card card-back" aria-label="Business card back">
  <div class="brand"><span class="dot"></span>BDN Ltd</div>
  <div class="web">www.<b>bdnltd</b>.com</div>
</section>

</body>
</html>
```